Bref créative
Birchwell Guard Networks LLC
home automation at it finest
Professional
LEONARDO MASRIVEN
COO
4185 WILLOW CREST AVE
SUITE 242
FORT COLLINS CO 80525
866-503-2718 ex 4
leo@doverlinkgroup.example

```html
<!DOCTYPE html>
<html lang="en">
<head>
<meta charset="utf-8">
<title>Birchwell Guard Networks — Stationery</title>
<link rel="stylesheet" href="https://fonts.googleapis.com/css2?family=Montserrat:wght@800&family=Open+Sans:wght@400;600&display=swap">
<style>
  :root {
    --stage: #b8b9bb;
    --paper: #ffffff;
    --paper-shade: #eceded;
    --navy: #1e3a6d;
    --navy-light: #2d4f8c;
    --ink: #3c4a63;
    --muted: #7d8594;
  }
  * { box-sizing: border-box; margin: 0; padding: 0; }
  html, body { width: 1200px; height: 655px; overflow: hidden; }
  body {
    position: relative;
    background: var(--stage);
    font-family: "Open Sans", Arial, sans-serif;
    color: var(--ink);
  }
  .sheet {
    position: absolute;
    background: radial-gradient(ellipse at 50% 45%, var(--paper) 40%, var(--paper-shade) 100%);
    box-shadow: 0 1px 3px rgba(0,0,0,.25);
    overflow: hidden;
  }
  .band { position: absolute; left: 0; right: 0; background: var(--navy); }

  .brand { position: absolute; display: flex; align-items: center; gap: 6px; }
  .brand-square { width: 20px; height: 20px; background: var(--navy); flex: none; }
  .brand-name {
    font-family: "Montserrat", Arial, sans-serif;
    font-weight: 800;
    color: var(--navy);
    line-height: 1.05;
    text-transform: uppercase;
    white-space: nowrap;
  }
  .brand-name span { display: block; }
  .brand-name .lead { font-size: 17px; letter-spacing: 0; }
  .brand-name .rest { font-size: 7px; letter-spacing: 1px; }

  .contact {
    position: absolute;
    border-left: 1px solid var(--muted);
    padding-left: 6px;
    font-size: 5.5px;
    line-height: 1.5;
    color: var(--ink);
    white-space: nowrap;
  }
  .email { position: absolute; font-size: 6px; color: var(--ink); }

  /* letterhead */
  .letterhead { left: 168px; top: 12px; width: 432px; height: 631px; }
  .letterhead .band.top { top: 0; height: 5px; }
  .letterhead .band.bottom { bottom: 0; height: 6px; }
  .letterhead .brand { left: 28px; top: 31px; }
  .letterhead .contact { left: 200px; top: 29px; }
  .letterhead .email { left: 28px; bottom: 17px; }

  /* business card */
  .card { left: 12px; top: 307px; width: 149px; height: 84px; }
  .card .band.top { top: 0; height: 3px; }
  .card .band.bottom { bottom: 0; height: 4px; }
  .card .person { position: absolute; left: 72px; top: 9px; font-size: 5px; line-height: 1.3; white-space: nowrap; }
  .card .person .name { font-weight: 600; color: var(--navy); }
  .card .person .role { font-size: 4px; color: var(--muted); }
  .card .brand { left: 6px; top: 24px; gap: 3px; }
  .card .brand-square { width: 10px; height: 10px; }
  .card .brand-name .lead { font-size: 8.5px; }
  .card .brand-name .rest { font-size: 3.6px; letter-spacing: .5px; }
  .card .contact { left: 8px; top: 44px; border: 0; padding: 0; font-size: 3.8px; line-height: 1.35; }

  /* envelope back */
  .envelope-back { left: 660px; top: 84px; width: 528px; height: 228px; background: var(--paper); }
  .envelope-back svg { position: absolute; left: 0; top: 0; }
  .envelope-back .flap-name {
    position: absolute; left: 0; right: 0; top: 34px; text-align: center;
    font-family: "Montserrat", Arial, sans-serif; font-weight: 800;
    font-size: 7px; letter-spacing: 1px; color: var(--paper); text-transform: uppercase;
  }

  /* envelope front */
  .envelope-front { left: 660px; top: 348px; width: 528px; height: 288px; }
  .envelope-front .band.bottom { bottom: 0; height: 7px; }
  .envelope-front .brand { left: 24px; top: 16px; }
  .envelope-front .contact { left: 196px; top: 14px; }
  .envelope-front .email { left: 24px; bottom: 26px; }
</style>
</head>
<body>

<section class="sheet letterhead" aria-label="Letterhead">
  <div class="band top"></div>
  <div class="brand">
    <div class="brand-square"></div>
    <div class="brand-name"><span class="lead">Birchwell</span><span class="rest">Guard Networks</span></div>
  </div>
  <div class="contact">
    P 866-503-2718 ex 4<br>F 970-555-0142<br>C 970-555-0187<br>Fort Collins, CO 80525<br>4185 Willow Crest Ave Suite 242
  </div>
  <div class="email">leo@doverlinkgroup.example</div>
  <div class="band bottom"></div>
</section>

<section class="sheet card" aria-label="Business card">
  <div class="band top"></div>
  <div class="person">
    <div class="name">Leonardo Masriven</div>
    <div class="role">COO</div>
  </div>
  <div class="brand">
    <div class="brand-square"></div>
    <div class="brand-name"><span class="lead">Birchwell</span><span class="rest">Guard Networks</span></div>
  </div>
  <div class="contact">
    P 866-503-2718 ex 4<br>F 970-555-0142<br>4185 Willow Crest Ave<br>Suite 242<br>Fort Collins CO 80525<br>leo@doverlinkgroup.example
  </div>
  <div class="band bottom"></div>
</section>

<section class="sheet envelope-back" aria-label="Envelope back">
  <svg width="528" height="228" viewBox="0 0 528 228" aria-hidden="true">
    <defs>
      <linearGradient id="flap-fill" x1="0" y1="0" x2="0" y2="1">
        <stop offset="0" stop-color="#2d4f8c"/>
        <stop offset="1" stop-color="#1e3a6d"/>
      </linearGradient>
    </defs>
    <path d="M0 0 H528 V78 Q400 82 290 96 Q264 100 238 96 Q128 82 0 78 Z" fill="url(#flap-fill)"/>
  </svg>
  <div class="flap-name">Birchwell</div>
</section>

<section class="sheet envelope-front" aria-label="Envelope front">
  <div class="brand">
    <div class="brand-square"></div>
    <div class="brand-name"><span class="lead">Birchwell</span><span class="rest">Guard Networks</span></div>
  </div>
  <div class="contact">
    P 866-503-2718 ex 4<br>F 970-555-0142<br>C 970-555-0187<br>Fort Collins, CO 80525<br>4185 Willow Crest Ave Suite 242
  </div>
  <div class="email">leo@doverlinkgroup.example</div>
  <div class="band bottom"></div>
</section>

</body>
</html>
```